mental health business card

Double sided business card with logo on front and practitioners details on back.
The front of card should be while and back either blue or grey to match logo.

Space on back for appointment date and time to be written.

Please note that details are not available yet for address etc as currently moving 4500km across Australia. Just use generic or old info from attached letterhead.
Updates

Dear Designers,

Please note business card is also appointment card must have area where  date and time of clients next appointment can be written in.

Target Market(s)

This is card for patients and colleagues

Industry/Entity Type

Mental Health

Requirements
Must have
• Name
Director / Clinical Psychologist
email
web
phone
phone

Nice to have
• embossing on front of card

```html
<!DOCTYPE html>
<html lang="en">
<head>
<meta charset="utf-8">
<title>Clearview Mental Health – Business Card</title>
<link rel="stylesheet" href="https://fonts.googleapis.com/css2?family=Open+Sans:wght@400;700&display=swap">
<style>
  :root {
    --backdrop: #d9d9d9;
    --card-white: #ffffff;
    --card-back: #ebebeb;
    --brand-grey: #808285;
    --brand-navy: #1b3a5e;
    --brand-deep: #15365a;
    --text-grey: #6d6e71;
    --rule-grey: #9a9a9a;
  }
  * { margin: 0; padding: 0; box-sizing: border-box; }
  html, body {
    width: 1200px;
    height: 900px;
    overflow: hidden;
    background: var(--backdrop);
  }
  .canvas {
    width: 1200px;
    height: 900px;
    display: flex;
    flex-direction: column;
    align-items: center;
    justify-content: center;
    gap: 56px;
  }
  .card {
    position: relative;
    width: 640px;
    height: 366px;
    overflow: hidden;
    box-shadow: 0 2px 6px rgba(0,0,0,0.12);
    font-family: "Open Sans", sans-serif;
  }
  .card--front { background: var(--card-white); }
  .card--back { background: var(--card-back); }

  .band {
    position: absolute;
    left: 0;
    right: 0;
  }
  .band--top {
    top: 0;
    height: 150px;
    background: var(--brand-grey);
  }
  .band--bottom {
    bottom: 0;
    height: 36px;
    background: var(--brand-deep);
  }

  .brand {
    position: absolute;
    display: flex;
    align-items: center;
    gap: 12px;
  }
  .brand__dot {
    width: 22px;
    height: 22px;
    border-radius: 50%;
    background: var(--brand-grey);
    flex: none;
  }
  .brand__name {
    font-size: 24px;
    font-weight: 400;
    color: var(--brand-navy);
    line-height: 1;
    white-space: nowrap;
  }
  .card--front .brand { right: 40px; top: 222px; }
  .card--back .brand { left: 40px; top: 142px; }
  .card--back .brand__dot { width: 18px; height: 18px; }
  .card--back .brand__name { font-size: 20px; }

  .practitioner {
    position: absolute;
    left: 420px;
    top: 30px;
  }
  .practitioner__name {
    font-size: 15px;
    font-weight: 700;
    color: var(--brand-navy);
    margin-bottom: 4px;
  }
  .practitioner__role {
    font-size: 9.5px;
    color: var(--text-grey);
    line-height: 1.4;
  }
  .appointment {
    position: absolute;
    left: 30px;
    right: 30px;
    bottom: 40px;
  }
  .appointment__line {
    border-bottom: 1px dashed var(--rule-grey);
    height: 34px;
  }
</style>
</head>
<body>
<main class="canvas">
  <section class="card card--front" aria-label="Card front">
    <div class="band band--top"></div>
    <div class="band band--bottom"></div>
    <div class="brand">
      <div class="brand__dot"></div>
      <p class="brand__name">Clearview Mental Health</p>
    </div>
  </section>

  <section class="card card--back" aria-label="Card back">
    <div class="practitioner">
      <p class="practitioner__name">Maren Holt</p>
      <p class="practitioner__role">Director<br>Clinical Psychologist</p>
    </div>
    <div class="brand">
      <div class="brand__dot"></div>
      <p class="brand__name">Clearview Mental Health</p>
    </div>
    <div class="appointment">
      <div class="appointment__line"></div>
      <div class="appointment__line"></div>
    </div>
  </section>
</main>
</body>
</html>
```